Cellar Crew Poster / Flyer Ad Design

We need a poster design (and a complimentary A6 flyer) to promote our Adult Rock Band Course called 'Cellar Crew'.

Target market is adults aged 25 - 50 primarily

Design to be eye catching, creative, appealing and easy to understand. Most of the distribution will be street marketing, email marketing, social media, music magazines and websites and to other music teachers.

We need the design to be as an A3 and A4 poster and an A6 promo flyer/e-flyer. Should look good in colour and we'll want a version in black and white.

Would be good to also incorporate our music school logo (just for branding purposes).

Text as follows:

CELLAR CREW
The Ultimate Rock Band Course for Adults

Ever wondered what it would be like to play in a band?

Feeling musically rusty and looking for a way to start playing your instrument again?

Then here’s an exciting opportunity you can’t miss!

All musical levels
Beginner/Intermediate to Advanced Players

Limited Numbers

REGISTER ONLINE NOW
www.tunewiseacademy.com.au

Starts Saturday 3rd August
Newtown

Over 6 exciting weekends you’ll work with one of our experienced professional band coaches and transform yourselves into the ultimate ‘Cellar Crew’

Discover how to play in a band
Revisit your musical abilities
Practice songs
Perform on Stage

Drummers, Bass Guitarists, Singers, Keys, Guitarists, Saxophone, Percussionists and others all welcome to join

For more information, course costs and registration, please visit www.tunewiseacademy.com.au or call 02 7194 2586 / 0432 987 654

Reason: Hi Everyone, I've been away and unable to respond to some of the designs because I've been ill. Have decided to extend the deadline and now commit to paying designers. Look forward to seeing more designs. Any questions, please let me know. Thanks Moira

```html
<!DOCTYPE html>
<html lang="en">
<head>
<meta charset="utf-8">
<title>Cellar Crew – The Ultimate Rock Band Course for Adults</title>
<link rel="stylesheet" href="https://fonts.googleapis.com/css2?family=Sniglet:wght@400;800&family=Rubik+Dirt&family=Alegreya+Sans:ital,wght@1,400&family=Open+Sans:ital,wght@0,400;1,400&display=swap">
<style>
  :root {
    --olive: #8f8338;
    --teal: #3fe3c9;
    --orange: #ea7a12;
    --ink: #161616;
    --navy: #14213a;
    --white: #ffffff;
    --brand-blue: #39a9d8;
  }
  * { margin: 0; padding: 0; box-sizing: border-box; }
  html, body { width: 848px; height: 1200px; overflow: hidden; background: var(--white); }
  .poster { position: relative; width: 848px; height: 1200px; overflow: hidden; font-family: "Sniglet", "Comic Sans MS", cursive; color: var(--ink); }

  .band { position: absolute; left: 0; width: 848px; }
  .band--intro { top: 0; height: 472px; }
  .band--title { top: 472px; height: 260px; background: var(--teal); }
  .band--details { top: 732px; height: 468px; }

  .instrument-pattern { position: absolute; inset: 0; }
  .band--intro .instrument-pattern { background: radial-gradient(circle at 50% 50%, #9a8d3e, var(--olive)); }
  .band--details .instrument-pattern { background: radial-gradient(circle at 50% 50%, #ef8420, var(--orange)); }

  .intro-copy { position: absolute; inset: 0; text-align: center; font-weight: 800; font-size: 25px; line-height: 1.18; }
  .intro-copy p { position: absolute; left: 0; width: 848px; }
  .intro-copy .left { text-align: left; left: 56px; width: 780px; }
  .q1 { top: 14px; }
  .q2 { top: 104px; }
  .q3 { top: 207px; }
  .levels { top: 288px; left: 0; font-size: 25px; }
  .register { top: 350px; color: var(--navy); font-size: 25px; line-height: 1.2; }

  .title { position: absolute; top: 20px; left: 0; width: 848px; text-align: center; font-family: "Rubik Dirt", "Impact", sans-serif; font-size: 84px; letter-spacing: 3px; color: var(--ink); }
  .tagline { position: absolute; top: 117px; left: 74px; font-family: "Alegreya Sans", "Optima", sans-serif; font-style: italic; font-size: 31px; color: var(--ink); }
  .contact { position: absolute; top: 188px; left: 0; width: 848px; text-align: center; font-family: "Open Sans", Arial, sans-serif; font-size: 16.5px; line-height: 1.3; color: var(--ink); }
  .contact em { font-style: italic; }

  .details-copy { position: absolute; top: 29px; left: 0; width: 848px; text-align: center; font-weight: 800; font-size: 25px; line-height: 1.22; }
  .details-copy .benefits { margin-top: 34px; }
  .details-copy .welcome { line-height: 1.2; }

  .brand { position: absolute; left: 556px; bottom: 4px; width: 290px; height: 55px; background: var(--white); display: flex; align-items: center; justify-content: center; gap: 12px; }
  .brand__name { font-family: "Sniglet", "Comic Sans MS", cursive; font-weight: 800; font-size: 24px; color: var(--brand-blue); }
  .brand__mark { width: 30px; height: 30px; background: var(--orange); border-radius: 50%; }
</style>
</head>
<body>
<main class="poster">
  <section class="band band--intro">
    <div class="instrument-pattern" role="img" aria-label="Repeating pattern of light green guitars, saxophones and other instruments on olive"></div>
    <div class="intro-copy">
      <p class="left q1">Ever wondered what it would be like to play in a band?</p>
      <p class="left q2">Feeling musically rusty and looking for a way to start playing your instrument again?</p>
      <p class="left q3">Then here’s an exciting opportunity you can’t miss!</p>
      <p class="levels">All musical levels : Beginner/Intermediate to Advanced Players</p>
      <p class="register">Limited Numbers REGISTER ONLINE NOW<br>www.tunewiseacademy.com.au<br>Starts Saturday 3rd August Newtown</p>
    </div>
  </section>

  <section class="band band--title">
    <h1 class="title">CELLAR CREW</h1>
    <p class="tagline">The Ultimate Rock Band Course for Adults</p>
    <p class="contact">For more information, course costs and registration,<br><em>please visit www.tunewiseacademy.com.au or call 02 7194 2586 / 0432 987 654</em></p>
  </section>

  <section class="band band--details">
    <div class="instrument-pattern" role="img" aria-label="Repeating pattern of light green guitars, saxophones and other instruments on orange"></div>
    <div class="details-copy">
      <p>Over 6 exciting weekends you’ll work with one of our<br>experienced professional band coaches and transform<br>yourselves into the ultimate ‘Cellar Crew’</p>
      <p class="benefits">Discover how to play in a band<br>Revisit your musical abilities<br>Practice songs<br>Perform on Stage</p>
      <p class="welcome">Drummers, Bass Guitarists, Singers, Keys, Guitarists,<br>Saxophone, Percussionists and others all welcome to join</p>
    </div>
    <div class="brand">
      <span class="brand__name">Tunewise Academy</span>
      <span class="brand__mark"></span>
    </div>
  </section>
</main>
</body>
</html>
```